New Sticker Design Project

Hello, Thank you for the great design of the tape. I would like to hire you to create another design to match the tape for the side of the box. 4" X 6"
Text: Perishable, Living Food as Medicine, Please Keep Cold, Do Not Delay, Quick Delivery Necessary, Place in Refrigerator Immediately upon Delivery
With symbols for Cold, and time-sensitive. Could use all caps if the design looks good. Same text font and color scheme to match the look of the tape. Logo if space. This needs to stand out on the shipping box which is brown boxes. Thanks again. !
Target Market(s)
Shipping box informational Sticker Outside
Requirements
Must have
- Similar matching look to the tape. The word PERISHABLE needs to be dominate!
Nice to have
- bold easy to read eye catching information for Parzo and customer
Should not have
- Clutter

```html
<!DOCTYPE html>
<html lang="en">
<head>
<meta charset="utf-8">
<title>Perishable Shipping Sticker</title>
<link href="https://fonts.googleapis.com/css2?family=Montserrat:wght@500;800;900&display=swap" rel="stylesheet">
<style>
  :root{
    --page:#ffffff;
    --paper:#efe6cc;
    --ink:#161a1a;
    --green:#0a7a35;
  }
  *{margin:0;padding:0;box-sizing:border-box}
  html,body{width:1200px;height:1200px;overflow:hidden;background:var(--page)}
  .sticker{
    position:absolute;left:279px;top:117px;width:646px;height:968px;
    background:var(--paper);font-family:"Montserrat",sans-serif;color:var(--ink);
  }
  .brand{position:absolute;left:210px;top:30px;display:flex;align-items:center;gap:12px}
  .brand-dot{width:30px;height:30px;border-radius:50%;background:var(--green)}
  .brand-name{font-weight:900;font-size:24px;line-height:27px;letter-spacing:-0.5px;text-align:center;white-space:nowrap}
  .alert-band{
    position:absolute;left:0;top:141px;width:646px;height:180px;background:var(--ink);color:var(--paper);
  }
  .alert-band .bang{position:absolute;top:46px;font-weight:800;font-size:80px;line-height:1}
  .alert-band .bang.left{left:40px}
  .alert-band .bang.right{left:580px}
  .alert-band .word{
    position:absolute;left:0;right:0;top:58px;text-align:center;
    font-weight:900;font-size:64px;letter-spacing:-1.5px;line-height:1;white-space:nowrap
  }
  .tagline{position:absolute;left:128px;top:352px;font-weight:500;font-size:52px;line-height:53px;letter-spacing:-0.5px;white-space:nowrap}
  .rule{position:absolute;left:58px;width:530px;height:8px;border-radius:4px;background:var(--ink)}
  .rule.top{top:473px}
  .rule.bottom{top:699px}
  .icon{position:absolute}
  .icon.cold{left:152px;top:497px;width:94px;height:92px}
  .icon.time{left:425px;top:500px;width:105px;height:90px}
  .notice{position:absolute;top:600px;color:var(--green);font-weight:900;font-size:42px;line-height:45px;text-align:center;letter-spacing:-1.5px;white-space:nowrap}
  .notice.cold{left:47px;width:300px}
  .notice.time{left:376px;width:200px}
  .step{position:absolute;left:0;width:646px;height:72px}
  .step.first{top:747px}
  .step.second{top:860px}
  .step-tag{position:absolute;left:0;top:0;width:94px;height:72px}
  .step-text{position:absolute;left:104px;top:2px;font-weight:900;font-size:32px;line-height:41px;letter-spacing:-0.8px;white-space:nowrap}
</style>
</head>
<body>
<div class="sticker">
  <div class="brand">
    <span class="brand-dot"></span>
    <span class="brand-name">GREEN LADLE<br>ALGAE</span>
  </div>

  <div class="alert-band">
    <span class="bang left">!</span>
    <span class="word">PERISHABLE</span>
    <span class="bang right">!</span>
  </div>

  <p class="tagline">LIVING FOOD<br>AS MEDICINE</p>

  <div class="rule top"></div>

  <svg class="icon cold" viewBox="0 0 94 92" fill="none" stroke="#0a7a35" stroke-width="4" stroke-linecap="round">
    <line x1="2" y1="12" x2="14" y2="12"/><line x1="2" y1="22" x2="10" y2="22"/>
    <line x1="2" y1="32" x2="14" y2="32"/><line x1="2" y1="42" x2="10" y2="42"/>
    <line x1="2" y1="52" x2="14" y2="52"/>
    <path d="M24 64V8a8 8 0 0 1 16 0v56a17 17 0 1 1 -16 0z"/>
    <circle cx="32" cy="75" r="6"/><line x1="32" y1="44" x2="32" y2="69"/>
    <g transform="translate(70 24)">
      <line x1="0" y1="-22" x2="0" y2="22"/><line x1="-19" y1="-11" x2="19" y2="11"/><line x1="-19" y1="11" x2="19" y2="-11"/>
      <path d="M-5 -18 0 -13 5 -18M-5 18 0 13 5 18M-18 -5 -11 -6 -14 -13M18 5 11 6 14 13M-18 5 -11 6 -14 13M18 -5 11 -6 14 -13"/>
    </g>
  </svg>

  <svg class="icon time" viewBox="0 0 105 90" fill="none" stroke="#0a7a35" stroke-width="4" stroke-linecap="round" stroke-linejoin="round">
    <path d="M44 6a10 10 0 0 1 17 0l40 68a8 8 0 0 1 -7 12H11a8 8 0 0 1 -7 -12z"/>
    <circle cx="55" cy="55" r="23"/><circle cx="55" cy="55" r="18" stroke-width="2"/>
    <path d="M55 55 48 47M55 55 64 53"/>
    <path d="M14 74h18M18 79h16M22 69h12" stroke-width="2"/>
  </svg>

  <p class="notice cold">PLEASE<br>KEEP COLD</p>
  <p class="notice time">DO NOT<br>DELAY</p>

  <div class="rule bottom"></div>

  <div class="step first">
    <svg class="step-tag" viewBox="0 0 94 72"><path d="M0 0H78L94 36 78 72H0z" fill="#161a1a"/></svg>
    <p class="step-text">QUICK DELIVERY<br>NECESSARY</p>
  </div>
  <div class="step second">
    <svg class="step-tag" viewBox="0 0 94 72"><path d="M0 0H78L94 36 78 72H0z" fill="#161a1a"/></svg>
    <p class="step-text">PLACE IN REFRIGERATOR<br>IMMEDIATELY UPON DELIVERY</p>
  </div>
</div>
</body>
</html>
```